Need innovative card design for tech start up

We are a Santa Monica based marketing analytics software start up called Meridel Pulse. We're launching a platform that will help advertisers better measure and optimize their marketing spend by using advanced algorithmic analytic. While our subject matter is complicated, we want to convey simple, clean, curated. We also want to stand out - ad tech is a sea of sameness and we need to have some individuality. We have an established color palette and would like to see a design we could print in each tone (teal, tangerine, grey), but it doesn't require the card to be monochromatic. The font used is DENSE.

Marketing

```html
<!DOCTYPE html>
<html lang="en">
<head>
<meta charset="utf-8">
<title>Meridel Pulse — Business Card</title>
<link href="https://fonts.googleapis.com/css2?family=Oswald:wght@300&display=swap" rel="stylesheet">
<style>
  :root {
    --tangerine: #fdbd00;
    --paper: #ffffff;
    --slate: #8e9d9d;
    --ink-light: #ffffff;
  }
  html, body {
    margin: 0;
    padding: 0;
    width: 1200px;
    height: 702px;
    overflow: hidden;
    background: var(--paper);
  }
  .card {
    position: relative;
    width: 1200px;
    height: 702px;
    font-family: "Oswald", "Arial Narrow", sans-serif;
    font-weight: 300;
  }
  .brand-panel {
    position: absolute;
    left: 0;
    top: 0;
    width: 498px;
    height: 702px;
    background: var(--paper);
  }
  .brand-square {
    position: absolute;
    left: 110px;
    top: 185px;
    width: 305px;
    height: 303px;
    background: var(--tangerine);
  }
  .brand-name {
    position: absolute;
    left: 0;
    width: 525px;
    top: 502px;
    text-align: center;
    font-size: 42px;
    line-height: 50px;
    color: var(--slate);
    text-transform: uppercase;
    letter-spacing: 0.5px;
    white-space: nowrap;
  }
  .info-panel {
    position: absolute;
    left: 498px;
    top: 0;
    width: 702px;
    height: 702px;
    background: var(--tangerine);
    color: var(--ink-light);
  }
  .info-block {
    position: absolute;
    left: 157px;
    margin: 0;
    font-size: 38px;
    line-height: 40px;
    letter-spacing: 0.6px;
    white-space: nowrap;
    font-style: normal;
  }
  .contact-name { top: 138px; }
  .contact-title { top: 193px; }
  .contact-address { top: 262px; }
  .contact-phones { top: 373px; }
  .contact-web { top: 485px; }
</style>
</head>
<body>
  <main class="card">
    <section class="brand-panel">
      <div class="brand-square"></div>
      <div class="brand-name">Meridel Pulse</div>
    </section>
    <section class="info-panel">
      <p class="info-block contact-name">Dorian Vashcombe</p>
      <p class="info-block contact-title">Founder/CEO</p>
      <address class="info-block contact-address">1840 Marlow Avenue, suite 310<br>Santa Monica, CA 90404</address>
      <p class="info-block contact-phones">office: 310-555-0147 x102<br>mobile: 310-555-0183</p>
      <p class="info-block contact-web">dorian@meridelpulse.com<br>www.meridelpulse.com</p>
    </section>
  </main>
</body>
</html>
```